Raised Fingerprint Business Card Design

I need a business card design and I would like the image for the business cards to carry on to my stationary and website. My business is Forensic Consulting. I will be providing services to prosecuting and defense attorneys as well as law enforcement agencies in the areas of latent print comparison, crime scene investigations, and forensic training. I am looking for a color scheme of red, black, and silver. I would like a fingerprint that is raised and the text to be raised to some degree depending on your recommendations. with a fingerprint glass. I would like the card to include the business name, my name the deignation CLPE after it, phone number, web address, and physical address. I would like the phrase "veritas aequitas " placed discretely at the bottome of the card-subtle/not too bold.

Target Market(s)

Attorneys and law enforcement agencies

Industry/Entity Type

Business

Contact Information for Business Card

Dora Pilcott, CLPE
Pilcott Trace Advisors, LLC
P.O. Box 731592 Sacramento, CA 95817
916.555.0148
www.pilcotttraceadvisors.com
pilcotttrace@mailvane.com

Colors
ec1f27

Requirements
Must have
• Fingerprint and old fashioned handheld magnifying glass (Barnaby Quist style.
• The Latin phrase listed above placed at the bottom of the front of the card discreetly.
Nice to have
• The fingerprint ridges (black lines) raised so the customer can feel it the texture.
• Raised lettering for either my name or the company name.
Should not have
• None that I can think of now.

```html
<!DOCTYPE html>
<html lang="en">
<head>
<meta charset="utf-8">
<title>Pilcott Trace Advisors — Business Card</title>
<link rel="stylesheet" href="https://fonts.googleapis.com/css2?family=Alegreya:wght@400;500&family=Exo+2:ital,wght@1,800&family=Josefin+Sans:wght@400;600&display=swap">
<style>
  :root {
    --backdrop: #e9e6e1;
    --card-frame: #0b0b0b;
    --card-face: #2a2a2b;
    --card-face-dark: #1f1f20;
    --ink-white: #f4f4f4;
    --ink-silver: #bdbdbd;
    --ink-muted: #9a9a9a;
    --accent-red: #c8202a;
    --accent-red-bright: #ec1f27;
    --band-white: #f7f7f7;
    --name-ink: #151515;
    --emblem-dark: #141414;
    --emblem-warm: #3b2c24;
  }
  * { box-sizing: border-box; margin: 0; padding: 0; }
  html, body { width: 1200px; height: 750px; overflow: hidden; }
  body {
    background: var(--backdrop);
    position: relative;
    font-family: "Josefin Sans", sans-serif;
  }

  .card {
    position: absolute;
    top: 217px;
    width: 540px;
    height: 315px;
    background: var(--card-frame);
    padding: 11px;
    box-shadow: 0 6px 18px rgba(0,0,0,0.28);
  }
  .card--front { left: 45px; }
  .card--back { left: 615px; }

  .card__face {
    position: relative;
    width: 100%;
    height: 100%;
    overflow: hidden;
    background:
      repeating-linear-gradient(0deg, rgba(255,255,255,0.018) 0 1px, transparent 1px 3px),
      radial-gradient(ellipse at 50% 40%, var(--card-face) 0%, var(--card-face-dark) 100%);
  }

  /* Front */
  .front__title {
    position: absolute;
    top: 22px; left: 0; right: 0;
    text-align: center;
    font-family: "Alegreya", serif;
    font-weight: 500;
    font-size: 30px;
    line-height: 1.18;
    color: var(--ink-white);
    text-shadow: 0 0 6px rgba(0,0,0,0.9), 0 2px 3px rgba(0,0,0,0.8);
  }
  .front__emblem {
    position: absolute;
    top: 100px; left: 225px;
    width: 270px; height: 135px;
    border-radius: 10px;
    background:
      radial-gradient(ellipse at 30% 50%, var(--emblem-dark) 0%, transparent 60%),
      radial-gradient(ellipse at 65% 50%, var(--emblem-warm) 0%, transparent 70%);
    opacity: 0.85;
  }
  .front__web {
    position: absolute;
    top: 246px; left: 0; right: 0;
    text-align: center;
    font-family: "Alegreya", serif;
    font-size: 15px;
    letter-spacing: 4.6px;
    color: var(--accent-red);
  }
  .front__motto {
    position: absolute;
    top: 272px; right: 30px;
    font-family: "Alegreya", serif;
    font-size: 8.5px;
    letter-spacing: 1.6px;
    color: var(--ink-muted);
  }

  /* Back */
  .back__graphics { position: absolute; inset: 0; }
  .back__name {
    position: absolute;
    top: 77px; right: 26px;
    font-family: "Exo 2", sans-serif;
    font-style: italic;
    font-weight: 800;
    font-size: 24px;
    letter-spacing: 0.5px;
    color: var(--name-ink);
  }
  .back__credential {
    position: absolute;
    top: 106px; right: 26px;
    font-family: "Alegreya", serif;
    font-weight: 500;
    font-size: 15px;
    letter-spacing: 0.5px;
    color: var(--accent-red);
  }
  .back__company {
    position: absolute;
    top: 140px; right: 42px;
    font-family: "Alegreya", serif;
    font-size: 17px;
    color: var(--accent-red);
  }
  .back__contacts {
    position: absolute;
    top: 192px; right: 40px;
    list-style: none;
    text-align: right;
  }
  .contact {
    display: flex;
    align-items: center;
    justify-content: flex-end;
    gap: 8px;
    height: 23px;
    font-size: 9px;
    letter-spacing: 0.6px;
    color: var(--ink-white);
  }
  .contact--address { font-variant: small-caps; font-size: 10px; }
  .contact__icon { width: 17px; height: 17px; flex: none; }
</style>
</head>
<body>

<section class="card card--front" aria-label="Business card front">
  <div class="card__face">
    <h1 class="front__title">Pilcott Trace<br>Advisors</h1>
    <div class="front__emblem" role="img" aria-label="Raised fingerprint seen through an old-fashioned handheld magnifying glass"></div>
    <p class="front__web">www.pilcotttraceadvisors.com</p>
    <p class="front__motto">veritas aequitas</p>
  </div>
</section>

<section class="card card--back" aria-label="Business card back">
  <div class="card__face">
    <svg class="back__graphics" viewBox="0 0 518 293" aria-hidden="true">
      <line x1="128" y1="0" x2="128" y2="42" stroke="var(--accent-red)" stroke-width="2"/>
      <circle cx="128" cy="44" r="4.5" fill="var(--accent-red)"/>
      <line x1="172" y1="0" x2="172" y2="30" stroke="var(--accent-red)" stroke-width="2"/>
      <circle cx="172" cy="32" r="4" fill="var(--accent-red)"/>
      <path d="M178 76 H518 V126 H178 A25 25 0 0 0 178 76 Z" fill="var(--band-white)"/>
      <line x1="150" y1="0" x2="150" y2="90" stroke="var(--ink-silver)" stroke-width="3"/>
      <circle cx="150" cy="101" r="12" fill="var(--band-white)" stroke="#8a8a8a" stroke-width="1"/>
      <line x1="0" y1="185" x2="518" y2="185" stroke="var(--ink-silver)" stroke-width="2"/>
      <line x1="0" y1="263" x2="140" y2="263" stroke="var(--accent-red)" stroke-width="2"/>
      <line x1="0" y1="271" x2="280" y2="271" stroke="var(--ink-silver)" stroke-width="2"/>
      <line x1="0" y1="281" x2="175" y2="281" stroke="var(--accent-red)" stroke-width="2"/>
    </svg>

    <p class="back__name">Dora Pilcott</p>
    <p class="back__credential">CLPE</p>
    <p class="back__company">Pilcott Trace Advisors</p>

    <ul class="back__contacts">
      <li class="contact contact--address">
        <span>P.O. Box 731592 Sacramento, CA 95817</span>
        <svg class="contact__icon" viewBox="0 0 20 20" aria-hidden="true">
          <circle cx="10" cy="10" r="9.5" fill="var(--accent-red-bright)"/>
          <path d="M10 4.5a3.3 3.3 0 0 0-3.3 3.3c0 2.4 3.3 6.7 3.3 6.7s3.3-4.3 3.3-6.7A3.3 3.3 0 0 0 10 4.5z" fill="none" stroke="#fff" stroke-width="1.3"/>
          <circle cx="10" cy="7.8" r="1.1" fill="#fff"/>
        </svg>
      </li>
      <li class="contact">
        <span>916.555.0148</span>
        <svg class="contact__icon" viewBox="0 0 20 20" aria-hidden="true">
          <circle cx="10" cy="10" r="9.5" fill="var(--accent-red-bright)"/>
          <path d="M7 5.2l1.7 2.4-1 1.2c.7 1.5 1.7 2.5 3.2 3.2l1.2-1 2.4 1.7-1 1.8c-3.7-.3-7-3.6-7.3-7.3z" fill="none" stroke="#fff" stroke-width="1.2" stroke-linejoin="round"/>
        </svg>
      </li>
      <li class="contact">
        <span>pilcotttrace@mailvane.com</span>
        <svg class="contact__icon" viewBox="0 0 20 20" aria-hidden="true">
          <circle cx="10" cy="10" r="9.5" fill="var(--accent-red-bright)"/>
          <rect x="5" y="6.5" width="10" height="7" fill="none" stroke="#fff" stroke-width="1.2"/>
          <path d="M5 6.5l5 4 5-4" fill="none" stroke="#fff" stroke-width="1.2"/>
        </svg>
      </li>
    </ul>
  </div>
</section>

</body>
</html>
```